Derek Holloway Plumbing and Heating

Need a card design for a plumbing and heating company that does service and repair, remodels, and plumbing in new construction. Please add following on back side of card; Boilers, Water heaters, Gas lines, Sump pumps, Toilet repairs, Faucet repairs, Pipe thawing, Radiant heating, New construction, Remodels.

Industry/Entity Type

Plumber

Contact Information for Business Card

Was thinking white gloss card with colored logo in middle or black glossy card with silver logo in middle. Just a thought but very open to other designs.

Requirements
Must have
• Need following on front of card;
• P(203) 321-8689
• C(203) 232-9069
• Derek Holloway 62 Marlow Ave North, Stamford, Ct 06455
• service@TorvenFlow.com (plumbing in blue, heating in red)
• www.TorvenFlow.com (plumbing in blue, heating in red)
• Fully Licensed and Insured
Nice to have
• Elegant design

```html
<!DOCTYPE html>
<html lang="en">
<head>
<meta charset="utf-8">
<title>Derek Holloway Plumbing and Heating – Business Card</title>
<link href="https://fonts.googleapis.com/css2?family=Saira:wght@400;500;700&family=PT+Sans:ital,wght@1,700&display=swap" rel="stylesheet">
<style>
  :root {
    --backdrop: #2b2b2b;
    --card-white: #f3f3f3;
    --blue-light: #3a8fd8;
    --blue-deep: #2e3596;
    --rim-dark: #2d46a8;
    --rim-light: #4fa6e6;
    --brand-blue: #2a3f9e;
    --brand-red: #c0283a;
    --grey-text: #555555;
    --white: #ffffff;
  }
  * { margin: 0; padding: 0; box-sizing: border-box; }
  html, body { width: 1200px; height: 960px; overflow: hidden; }
  body { background: var(--backdrop); position: relative; font-family: "Saira", sans-serif; }

  .card { position: absolute; width: 600px; height: 343px; border-radius: 18px; overflow: hidden; }
  .card-front { left: 314px; top: 113px; }
  .card-back { left: 311px; top: 472px; background: var(--card-white); }
  .card-shape { position: absolute; inset: 0; }

  .contact { position: absolute; left: 29px; top: 58px; color: var(--white); }
  .contact-name { font-weight: 700; font-size: 19px; line-height: 22px; letter-spacing: 0.2px; }
  .contact-role { font-size: 14px; line-height: 18px; margin-bottom: 24px; }
  .contact-line { font-size: 14px; line-height: 18.5px; display: flex; align-items: center; gap: 6px; }
  .contact-line svg { width: 13px; height: 13px; flex: none; }
  .group { margin-bottom: 10px; }

  .brand { position: absolute; text-align: center; color: var(--brand-blue); font-weight: 700; }
  .brand-mark { display: block; margin: 0 auto 8px; border-radius: 50%; background: var(--brand-blue); }
  .brand-name { font-size: 20px; line-height: 22px; letter-spacing: 1.5px; text-transform: uppercase; }
  .brand-web { display: block; margin-top: 6px; font-size: 11px; font-weight: 500; color: var(--grey-text); }

  .brand-front { left: 300px; top: 102px; width: 290px; }
  .brand-front .brand-mark { width: 46px; height: 46px; }
  .brand-front .brand-name { font-size: 17px; line-height: 20px; }

  .brand-back { left: 0; top: 48px; width: 600px; }
  .brand-back .brand-mark { width: 70px; height: 70px; margin-bottom: 12px; }
  .brand-back .brand-name { font-size: 22px; line-height: 24px; }

  .services { position: absolute; left: 0; top: 226px; width: 600px; text-align: center; font-family: "PT Sans", sans-serif; font-style: italic; font-weight: 700; }
  .services-title { font-size: 19px; color: var(--blue-deep); line-height: 26px; margin-bottom: 2px; }
  .services-list { font-size: 13.5px; color: var(--grey-text); line-height: 18px; }
  .dot { color: var(--blue-deep); }
</style>
</head>
<body>
  <section class="card card-front" aria-label="Card front">
    <svg class="card-shape" viewBox="0 0 600 343" aria-hidden="true">
      <defs>
        <linearGradient id="frontBlue" x1="0" y1="0" x2="0" y2="1">
          <stop offset="0" stop-color="var(--blue-light)"/>
          <stop offset="1" stop-color="var(--blue-deep)"/>
        </linearGradient>
      </defs>
      <rect width="600" height="343" fill="url(#frontBlue)"/>
      <ellipse cx="620" cy="171" rx="346" ry="202" fill="var(--rim-dark)"/>
      <ellipse cx="620" cy="171" rx="338" ry="196" fill="var(--rim-light)"/>
      <ellipse cx="620" cy="171" rx="332" ry="192" fill="var(--card-white)"/>
    </svg>

    <div class="contact">
      <p class="contact-name">DEREK HOLLOWAY</p>
      <p class="contact-role">OWNER</p>
      <div class="group">
        <p class="contact-line">62 Marlow Ave North</p>
        <p class="contact-line">Stamford, Ct 06455</p>
      </div>
      <div class="group">
        <p class="contact-line"><svg viewBox="0 0 16 16"><path fill="#fff" d="M3.5 1.5l2.5 0 1.2 3.3-1.6 1.2c.8 1.7 2.2 3.1 3.9 3.9l1.2-1.6 3.3 1.2v2.5c0 1-1 1.8-2 1.7C6.7 13.4 2.6 9.3 1.8 3.5 1.7 2.5 2.5 1.5 3.5 1.5z"/></svg>(203) 555-4172</p>
        <p class="contact-line"><svg viewBox="0 0 16 16"><rect x="4" y="1" width="8" height="14" rx="1.5" fill="none" stroke="#fff" stroke-width="1.6"/><rect x="7" y="12" width="2" height="1.2" fill="#fff"/></svg>(203) 555-7830</p>
        <p class="contact-line"><svg viewBox="0 0 16 16"><rect x="1.5" y="4" width="13" height="9" fill="#fff"/><path d="M1.5 4l6.5 5 6.5-5" fill="none" stroke="#2e3596" stroke-width="1.2"/></svg>service@TorvenFlow.com</p>
      </div>
      <p class="contact-line">Master Plumbing License 518630</p>
      <p class="contact-line">Master Heating/AC License 742915</p>
    </div>

    <div class="brand brand-front">
      <span class="brand-mark" aria-hidden="true"></span>
      <p class="brand-name">Derek Holloway<br>Plumbing and Heating</p>
      <span class="brand-web">www.TorvenFlow.com</span>
    </div>
  </section>

  <section class="card card-back" aria-label="Card back">
    <div class="brand brand-back">
      <span class="brand-mark" aria-hidden="true"></span>
      <p class="brand-name">Derek Holloway<br>Plumbing and Heating</p>
      <span class="brand-web">www.TorvenFlow.com</span>
    </div>
    <div class="services">
      <p class="services-title">Fully Licensed and Insured</p>
      <p class="services-list">Boilers <span class="dot">•</span> Water heaters <span class="dot">•</span> Gas lines <span class="dot">•</span> Sump pumps <span class="dot">•</span> Toilet repairs</p>
      <p class="services-list">Faucet repairs <span class="dot">•</span> Pipe thawing <span class="dot">•</span> Radiant heating</p>
      <p class="services-list">New construction <span class="dot">•</span> Remodels.</p>
    </div>
  </section>
</body>
</html>
```